" A proprietária é a Lorena Bastolli, Biomedica, pós graduada em estética e Mestra pela Universidade de Vale Dourado. Temos trabalhando conosco uma fisioterapeuta, uma esteticista, uma estagiária em biomedica, uma secretária, e temos parceria com uma Nutricionista com PHD e uma Médica especialista em Endocrinologia, ambas atendem na clínica uma vez por semana. "

```html
<!DOCTYPE html>
<html lang="pt-BR">
<head>
<meta charset="UTF-8">
<title>Lorena Bastolli – Blocos de Anotação</title>
<link href="https://fonts.googleapis.com/css2?family=Cormorant+Garamond:wght@500;600&family=Montserrat:wght@400;500&display=swap" rel="stylesheet">
<style>
  :root {
    --backdrop: #e9e9e9;
    --ink-dark: #1d1d24;
    --paper: #ffffff;
    --gold: #c9a15a;
    --gold-soft: rgba(201, 161, 90, 0.45);
    --rule: #6f6f76;
    --text-grey: #5c5c63;
  }
  * { margin: 0; padding: 0; box-sizing: border-box; }
  html, body {
    width: 1200px; height: 1200px; overflow: hidden;
    background: var(--backdrop);
  }
  .stationery {
    position: relative; width: 1200px; height: 1200px;
  }
  .pad {
    position: absolute; top: 372px; width: 312px; height: 590px;
    box-shadow: 0 6px 14px rgba(0,0,0,0.12);
    overflow: hidden;
  }
  .pad--cover { left: 96px; background: var(--ink-dark); }
  .pad--letterhead { left: 444px; background: var(--paper); }
  .pad--lined { left: 792px; background: var(--paper); }

  /* cover */
  .cover-brand {
    position: absolute; top: 40px; left: 0; width: 100%;
    display: flex; flex-direction: column; align-items: center;
  }
  .brand-mark {
    width: 22px; height: 22px; border-radius: 50%;
    border: 1.5px solid var(--gold); margin-bottom: 10px;
  }
  .brand-name {
    font-family: "Cormorant Garamond", serif; font-weight: 600;
    font-size: 25px; color: #ffffff; letter-spacing: 0.3px;
  }
  .brand-tagline {
    font-family: "Montserrat", sans-serif; font-size: 7px;
    color: var(--gold); letter-spacing: 2px; text-transform: uppercase;
    margin-top: 5px;
  }
  .cover-accent {
    position: absolute; left: -110px; top: 200px;
    width: 260px; height: 260px; border-radius: 50%;
    border: 2px solid var(--gold-soft);
  }

  /* letterhead */
  .letterhead-contact {
    position: absolute; left: 22px; bottom: 42px;
    display: flex; gap: 14px;
    font-family: "Montserrat", sans-serif; font-size: 5.5px;
    color: var(--text-grey); line-height: 1.6;
  }
  .contact-item { display: flex; gap: 4px; align-items: flex-start; }
  .contact-item svg { flex: none; margin-top: 1px; }
  .letterhead-accent {
    position: absolute; right: -40px; bottom: -30px;
    width: 180px; height: 180px; border-radius: 50%;
    border: 1.5px solid var(--gold-soft);
  }

  /* lined sheet */
  .lined-header {
    position: absolute; top: 24px; left: 22px; right: 22px;
    border-bottom: 1.5px solid var(--gold);
    height: 14px;
  }
  .lined-header span {
    position: absolute; right: 0; top: 0;
    font-family: "Montserrat", sans-serif; font-size: 5.5px;
    color: var(--gold); letter-spacing: 1px;
  }
  .lined-rules {
    position: absolute; top: 52px; left: 22px; right: 22px; bottom: 48px;
    background: repeating-linear-gradient(
      to bottom, transparent 0, transparent 16px, var(--rule) 16px, var(--rule) 17px);
  }
  .lined-footer {
    position: absolute; left: 0; right: 0; bottom: 0; height: 14px;
    background: var(--gold);
  }
</style>
</head>
<body>
<main class="stationery">

  <section class="pad pad--cover">
    <div class="cover-brand">
      <div class="brand-mark"></div>
      <div class="brand-name">Lorena Bastolli</div>
      <div class="brand-tagline">Biomedicina Estética</div>
    </div>
    <div class="cover-accent"></div>
  </section>

  <section class="pad pad--letterhead">
    <div class="letterhead-contact">
      <div class="contact-item">
        <svg width="7" height="7" viewBox="0 0 10 10"><path d="M2 1 L4 1 L5 3.5 L3.8 4.5 Q5 6.5 6 6.8 L7 5.8 L9 7 L9 9 Q4 9.5 1 2 Z" fill="#c9a15a"/></svg>
        <div>(16) 3000-0000<br>(16) 90000-0000<br>lorenabastolli.com.br</div>
      </div>
      <div class="contact-item">
        <svg width="6" height="8" viewBox="0 0 8 11"><path d="M4 0 A4 4 0 0 1 8 4 C8 7 4 11 4 11 C4 11 0 7 0 4 A4 4 0 0 1 4 0 Z" fill="#c9a15a"/><circle cx="4" cy="4" r="1.5" fill="#fff"/></svg>
        <div>Rua das Acácias, 120 - Centro<br>Vale Dourado - SP</div>
      </div>
    </div>
    <div class="letterhead-accent"></div>
  </section>

  <section class="pad pad--lined">
    <div class="lined-header"><span>Lorena Bastolli</span></div>
    <div class="lined-rules"></div>
    <div class="lined-footer"></div>
  </section>

</main>
</body>
</html>
```